Inspirational Card with Words of Wisdom to Give to Kids

I run basketball camps and give inspirational messages to elementary schools and high schools (www.pastthebrightline.net).

I would like to create a card that has some inspirational thoughts and words of wisdom on it that I can give away...and that students and athletes will keep in their wallet as a reminder of things I've taught them.

I want it to be clean and classy, while not looking too child-like or business-like, as I'd like to be able to give it out to kids, teenagers, and young adults.

The card will be the size of a regular business card and will be double-sided. I would like to use black, orange, gray, and white as the primary colors, with white or gray likely being the background color.
Updates

You're welcome to leave off the title "Wisdom for Life" if desired and just use "The Triple Crown of Success" on the front of the card.

Thanks.

If you choose to leave off the poem, which you're welcome to do, please make one minor addition to the 5-point creed:

Add the words "God and" to "Honour others in everything you say and do" so it becomes:

"Honour God and others in everything you say and do."

Target Market(s)

Children, Teenagers, and Young Adults

Industry/Entity Type

Business

Requirements
Must have
• All the content, although the poem could be removed if necessary.
Should not have
• Nothing basketball-specific, as I want to be able to give it out to any child or teenager.

```html
<!DOCTYPE html>
<html lang="en">
<head>
<meta charset="utf-8">
<title>Wisdom for Life – Card Front and Back</title>
<link rel="stylesheet" href="https://fonts.googleapis.com/css2?family=Chakra+Petch:wght@600&family=Tinos:ital,wght@0,400;0,700;1,400;1,700&family=Open+Sans:ital,wght@0,400;0,700;1,400&display=swap">
<style>
  :root {
    --orange: #ff4d00;
    --ink: #111111;
    --band: #c0c0c0;
    --edge: #b8b8b8;
    --paper: #ffffff;
  }
  * { box-sizing: border-box; margin: 0; padding: 0; }
  html, body { width: 1200px; height: 414px; overflow: hidden; background: var(--paper); }
  body { position: relative; font-family: "Tinos", "Times New Roman", serif; color: var(--ink); }

  .side-label {
    position: absolute; top: 10px; width: 300px; text-align: center;
    font: 700 36px/1 "Tinos", serif; color: var(--orange); letter-spacing: 0.5px;
  }
  .side-label--front { left: 112px; }
  .side-label--back { left: 761px; }

  .card {
    position: absolute; top: 61px; width: 578px; height: 331px;
    border: 1px solid var(--edge); background: var(--paper); overflow: hidden;
  }
  .card--front { left: 13px; }
  .card--back { left: 604px; width: 581px; }
  .card > * { position: absolute; }

  .card__band {
    left: 0; right: 0; bottom: 0; height: 67px; background: var(--band);
    text-align: center;
  }

  /* FRONT */
  .title {
    left: 0; right: 0; top: 17px; text-align: center;
    font: 600 26px/1 "Chakra Petch", sans-serif; color: var(--orange); letter-spacing: 1.5px;
  }
  .title .stars { font-size: 18px; letter-spacing: 3px; vertical-align: 3px; }
  .crown-heading { left: 22px; top: 76px; font: 700 15px/1 "Tinos", serif; letter-spacing: 1.2px; }
  .rule-label { font: 600 11.5px/1 "Chakra Petch", sans-serif; color: var(--orange); letter-spacing: 0.5px; }
  .rule-item { font: 700 12.5px/1 "Tinos", serif; white-space: nowrap; }
  .rule-item::before { content: "☞"; font-weight: 400; margin-right: 1px; }

  .poem-heading { left: 307px; top: 71px; font: 700 14.5px/1 "Tinos", serif; }
  .poem { right: 19px; top: 92px; text-align: right; font: italic 400 13.6px/20px "Open Sans", sans-serif; }
  .poem .lead { color: var(--orange); }
  .poem-credit { right: 20px; top: 193px; font: italic 400 10px/1 "Open Sans", sans-serif; }

  .quote { margin-top: 7px; font: 400 16px/1.2 "Open Sans", sans-serif; color: var(--orange); }
  .quote-credit { margin-top: 3px; font: 700 13.5px/1.2 "Open Sans", sans-serif; }
  .quote-credit em { font-weight: 400; font-size: 11px; }

  /* BACK */
  .creed-heading { left: 21px; top: 22px; font: 700 13px/1 "Tinos", serif; color: var(--orange); }
  .creed { left: 21px; top: 39px; list-style: none; font: 400 13px/18px "Tinos", serif; }
  .creed span { font-size: 11px; margin-right: 3px; }
  .pledge-heading { right: 25px; top: 132px; font: 700 12.5px/1 "Tinos", serif; color: var(--orange); }
  .pledge { right: 25px; top: 150px; text-align: right; font: italic 400 12.5px/17px "Open Sans", sans-serif; }
  .sign-line { right: 25px; width: 172px; border-top: 1px solid var(--ink); text-align: right;
    font: italic 400 10.5px/1 "Open Sans", sans-serif; padding-top: 5px; }
  .sign-line--signature { top: 203px; }
  .sign-line--date { top: 240px; }

  .motto { margin-top: 6px; font: italic 400 15px/1.2 "Open Sans", sans-serif; color: var(--orange); }
  .virtues { margin-top: 6px; font: 700 13.5px/1.2 "Tinos", serif; word-spacing: 1px; }
  .virtues .dot { color: var(--orange); font-size: 11px; margin: 0 4px; vertical-align: 1px; }
</style>
</head>
<body>
  <div class="side-label side-label--front">FRONT</div>
  <div class="side-label side-label--back">BACK</div>

  <section class="card card--front">
    <h1 class="title"><span class="stars">✷✷✷</span> WISDOM FOR LIFE <span class="stars">✷✷✷</span></h1>

    <h2 class="crown-heading">The Triple Crown of Success;</h2>
    <div class="rule-label" style="left:22px;top:98px">NEVER</div>
    <div class="rule-item" style="left:22px;top:116px">Lie</div>
    <div class="rule-item" style="left:22px;top:137px">Cheat</div>
    <div class="rule-item" style="left:22px;top:157px">Steal</div>

    <div class="rule-label" style="left:196px;top:98px">DON'T</div>
    <div class="rule-item" style="left:196px;top:116px">Blame</div>
    <div class="rule-item" style="left:196px;top:137px">Complain</div>
    <div class="rule-item" style="left:196px;top:157px">Give Up</div>

    <div class="rule-label" style="left:116px;top:159px">ALWAYS</div>
    <div class="rule-item" style="left:102px;top:179px">Be Grateful</div>
    <div class="rule-item" style="left:98px;top:199px">Uplift Others</div>
    <div class="rule-item" style="left:59px;top:220px">Do More Than Your Share</div>

    <h2 class="poem-heading">Four things a man must learn to do</h2>
    <p class="poem">
      <span class="lead">If he would make his life more true:</span><br>
      To think without confusion clearly,<br>
      To love his fellow man sincerely,<br>
      To act from honest motives purely,<br>
      To trust in God and Heaven securely.
    </p>
    <p class="poem-credit">Rev. Samuel Ashby</p>

    <footer class="card__band">
      <p class="quote">“Make each day your masterpiece”</p>
      <p class="quote-credit">- Coach Walt Harmon <em>(The source of inspiration for this card)</em></p>
    </footer>
  </section>

  <section class="card card--back">
    <h2 class="creed-heading">A 5–Point Creed</h2>
    <ol class="creed">
      <li><span>1.</span>Be intentional to grow and learn new things each day.</li>
      <li><span>2.</span>Honour others in everything you say and do.</li>
      <li><span>3.</span>Act with integrity and uprightness in all matters.</li>
      <li><span>4.</span>Prioritize serving and giving to others above yourself.</li>
      <li><span>5.</span>Dream, pray, and expect for the impossible.</li>
    </ol>

    <h2 class="pledge-heading">Triple Crown &amp; 5–Point Creed Pledge:</h2>
    <p class="pledge">I commit to doing my best to live out<br>the Triple Crown and 5-Point Creed each day.</p>
    <div class="sign-line sign-line--signature">Signature</div>
    <div class="sign-line sign-line--date">Date</div>

    <footer class="card__band">
      <p class="motto">Live every day with:</p>
      <p class="virtues"><span class="dot">✷</span>Passion <span class="dot">✷</span>Wonder <span class="dot">✷</span>Playfulness <span class="dot">✷</span>Gratitude <span class="dot">✷</span>Love <span class="dot">✷</span></p>
    </footer>
  </section>
</body>
</html>
```